Dale Harwick Terrain Services LLC

Need a business card design for a new company based in Harlow Springs, MS. We specialize in under-brush clearing, forestry mulching, cutover mulching, right of way clearing, land line & fence row clearing, bush hogging, land clearing, wildlife food plots. We use compact track loaders and tractors. I will attach a picture of a compact track loader I would like to have on the card design if possible.

Target Market(s)

Businesses / Land Owners

Contact Information for Business Card

Dale Harwick
Owner / Operator

Harlow Springs, MS

Call/Text: 601-555-3871
dhterrainwork@mailvista.test
FB: @daleharwickterrainservicesllc

Font styles to use
Serif
Sans Serif

Requirements
Must have
• Contact info, city & state. Description of services.
Nice to have
• Not overwhelming back ground but eye and interest catching with clear objection of the business

```html
<!DOCTYPE html>
<html lang="en">
<head>
<meta charset="utf-8">
<title>Dale Harwick Terrain Services LLC — Business Card</title>
<link href="https://fonts.googleapis.com/css2?family=Poppins:wght@500;600;700&family=Exo+2:wght@500;600&display=swap" rel="stylesheet">
<style>
  :root {
    --backdrop: #e9e4dc;
    --card-black: #141414;
    --brand-red: #e02327;
    --deep-red: #8e1113;
    --white: #ffffff;
    --ink: #1a1a1a;
    --photo-yellow: #c9951e;
    --photo-green: #5d7a34;
    --photo-shadow: #2a2a22;
  }
  * { margin: 0; padding: 0; box-sizing: border-box; }
  html, body { width: 900px; height: 1200px; overflow: hidden; }
  body { background: var(--backdrop); position: relative; font-family: "Poppins", sans-serif; }

  .card {
    position: absolute; left: 103px; width: 705px; height: 413px;
    background: var(--card-black); overflow: hidden;
    box-shadow: 0 6px 18px rgba(0,0,0,.35);
  }
  .card--front { top: 160px; }
  .card--back { top: 636px; }

  /* front */
  .front-photo {
    position: absolute; left: 0; top: 0; width: 480px; height: 320px;
    background: linear-gradient(160deg, var(--photo-shadow) 0%, #3a3626 35%, var(--photo-yellow) 58%, var(--photo-green) 90%);
    clip-path: polygon(0 0, 99.5% 0, 62% 100%, 0 100%);
  }
  .front-stripe { position: absolute; left: 0; top: 0; width: 705px; height: 320px; }
  .brand-mark {
    position: absolute; left: 477px; top: 100px; width: 135px;
    display: flex; align-items: center; justify-content: center; gap: 8px;
    color: var(--white); font-weight: 700; font-size: 34px; letter-spacing: 1px; line-height: 1;
  }
  .brand-mark .mark-square { width: 14px; height: 14px; background: var(--brand-red); flex: none; }
  .front-title {
    position: absolute; left: 400px; top: 182px; width: 290px; text-align: center; color: var(--white);
  }
  .company-name { font-size: 31px; font-weight: 700; line-height: 1; letter-spacing: .5px; white-space: nowrap; }
  .company-name .accent { color: var(--brand-red); }
  .company-sub { font-size: 16px; font-weight: 600; letter-spacing: .6px; margin-top: 4px; white-space: nowrap; }
  .company-city { font-size: 15px; font-weight: 600; letter-spacing: .8px; margin-top: 10px; }

  .owner-band {
    position: absolute; left: 0; top: 320px; width: 705px; height: 50px; background: var(--card-black);
  }
  .owner-name { position: absolute; left: 44px; top: 5px; color: var(--white); font-size: 20px; font-weight: 600; letter-spacing: .5px; }
  .owner-role { position: absolute; left: 44px; top: 30px; color: var(--brand-red); font-size: 12px; font-weight: 600; letter-spacing: .6px; }
  .phone-band {
    position: absolute; left: 295px; top: 320px; width: 410px; height: 50px; background: var(--brand-red);
    clip-path: polygon(0 0, 100% 0, 100% 100%, 12px 100%);
    display: flex; align-items: center; gap: 10px; padding-left: 36px;
    color: var(--white); font-size: 30px; font-weight: 500;
  }
  .phone-band svg { flex: none; }
  .contact-row { position: absolute; left: 0; top: 370px; width: 705px; height: 43px; }
  .contact-email {
    position: absolute; left: 0; top: 0; width: 360px; height: 43px; background: var(--white);
    clip-path: polygon(0 0, 100% 0, 94% 100%, 0 100%);
    display: flex; align-items: center; gap: 8px; padding-left: 44px;
    color: var(--ink); font-size: 14px;
  }
  .contact-social {
    position: absolute; left: 368px; top: 0; height: 43px;
    display: flex; align-items: center; gap: 8px;
    color: var(--white); font-size: 14.5px;
  }
  .social-dot { width: 12px; height: 12px; border-radius: 50%; background: var(--white); }

  /* back */
  .back-photo {
    position: absolute; right: 0; top: 0; width: 360px; height: 413px;
    background: linear-gradient(160deg, #1f2a1c 0%, #3b3a2c 40%, var(--photo-yellow) 70%, var(--photo-green) 100%);
    -webkit-mask-image: linear-gradient(90deg, transparent 0%, #000 30%);
            mask-image: linear-gradient(90deg, transparent 0%, #000 30%);
  }
  .back-title { position: absolute; left: 35px; top: 47px; color: var(--white); }
  .back-title .company-name { font-size: 37px; letter-spacing: .5px; }
  .back-title .company-sub { font-size: 18.5px; margin-top: 2px; letter-spacing: .7px; }
  .service-list { position: absolute; left: 37px; top: 158px; list-style: none; }
  .service-list li {
    display: flex; align-items: center; gap: 12px; height: 27.3px;
    color: var(--white); font-family: "Exo 2", sans-serif; font-weight: 500;
    font-size: 16px; letter-spacing: 1.2px; text-transform: uppercase;
  }
  .service-list li::before { content: ""; width: 9px; height: 9px; background: var(--brand-red); flex: none; }
</style>
</head>
<body>

<section class="card card--front">
  <div class="front-photo" role="img" aria-label="Photo of a yellow compact track loader with a forestry mulcher attachment on grass"></div>
  <svg class="front-stripe" viewBox="0 0 705 320" aria-hidden="true">
    <defs>
      <linearGradient id="stripe-fade" x1="0" y1="0" x2="1" y2="0.4">
        <stop offset="0" stop-color="#8e1113" stop-opacity="0"/>
        <stop offset="0.6" stop-color="#b81a1e" stop-opacity="0.8"/>
        <stop offset="1" stop-color="#e02327"/>
      </linearGradient>
    </defs>
    <polygon points="330,0 478,0 362,176 300,176" fill="url(#stripe-fade)"/>
  </svg>

  <div class="brand-mark"><span class="mark-square"></span>DHTS</div>

  <div class="front-title">
    <div class="company-name">DALE <span class="accent">HARWICK</span></div>
    <div class="company-sub">TERRAIN SERVICES LLC</div>
    <div class="company-city">HARLOW SPRINGS, MS</div>
  </div>

  <div class="owner-band">
    <div class="owner-name">DALE HARWICK</div>
    <div class="owner-role">OWNER / OPERATOR</div>
  </div>
  <div class="phone-band">
    <svg width="30" height="28" viewBox="0 0 30 28" aria-hidden="true">
      <path d="M6 4c2 0 4 4 4 5s-2 2-2 3 3 5 5 6c1 0 2-2 3-2s5 2 5 4-2 4-4 4C10 24 2 14 2 8c0-2 2-4 4-4z" fill="#fff"/>
    </svg>
    <svg width="30" height="28" viewBox="0 0 30 28" aria-hidden="true">
      <rect x="4" y="3" width="22" height="16" rx="3" fill="#fff"/>
      <polygon points="8,18 8,25 14,18" fill="#fff"/>
      <rect x="9" y="8" width="12" height="2" fill="#e02327"/>
      <rect x="9" y="12" width="9" height="2" fill="#e02327"/>
    </svg>
    <span>601-555-3871</span>
  </div>
  <div class="contact-row">
    <div class="contact-email">
      <svg width="15" height="11" viewBox="0 0 15 11" aria-hidden="true">
        <rect width="15" height="11" fill="#e02327"/>
        <polyline points="0,0 7.5,6 15,0" fill="none" stroke="#fff" stroke-width="1.3"/>
      </svg>
      <span>dhterrainwork@mailvista.test</span>
    </div>
    <div class="contact-social"><span class="social-dot"></span><span>@daleharwickterrainservicesllc</span></div>
  </div>
</section>

<section class="card card--back">
  <div class="back-photo" role="img" aria-label="Photo of the compact track loader's mulching head cutting across a grassy field"></div>
  <div class="back-title">
    <div class="company-name">DALE <span class="accent">HARWICK</span></div>
    <div class="company-sub">TERRAIN SERVICES LLC</div>
  </div>
  <ul class="service-list">
    <li>Under-brush clearing</li>
    <li>Forestry mulching</li>
    <li>Cutover mulching</li>
    <li>Right of way clearing</li>
    <li>Land line, fence row clearing</li>
    <li>Bush hogging</li>
    <li>Land clearing</li>
    <li>Wildlife food plots</li>
  </ul>
</section>

</body>
</html>
```